Custom Flooring Website For Tulsa Oklahoma Flooring Store

We need to a design for a website that is in between these two current designs, with a modern look and feel.

https://www.talvenfloors.com/
https://mirelopaving.ca/
We need a home page and 2 interior page styles designed.

Talven Flooring is a locally owned flooring company based in Tulsa, Oklahoma. The website should reflect a professional, established business that sells high-quality flooring products, provides expert installation, and specializes in hardwood floor refinishing. The goal of the site is to clearly communicate trust, craftsmanship, and ease of doing business, while guiding users toward visiting the showroom or requesting service.

The company operates a physical showroom in Tulsa where customers can browse flooring materials in person. Talven Flooring sells five primary product categories: solid hardwood, engineered hardwood, laminate, luxury vinyl plank (LVP), and tile. Tile includes both wall and floor applications, as well as decorative options such as glass tile, metal tile, and natural stone. In addition to product sales, the company offers professional flooring installation, hardwood floor refinishing, and water damage restoration related to flooring.

The website structure is intentionally segmented into three main areas: product pages, service pages, and informational pages (About, Financing, Homepage). Product pages focus on education and selection, helping users understand differences between materials and where they work best. Service pages use a more process-driven layout that explains what to expect before, during, and after work is performed. The homepage serves as an overview, positioning Talven Flooring as a full-service flooring store, tile store, and contractor serving Tulsa and surrounding areas.

Visually, the site should feel clean, approachable, and confidence-inspiring—never flashy or overly sales-driven. The design should support browsing materials, understanding services, and contacting the company easily. Strong emphasis should be placed on clear navigation, readable typography, and a layout that works equally well on desktop and mobile devices.

Calls to action should focus on visiting the showroom, scheduling consultations, and exploring flooring options. The financing page should feel simple and reassuring, reducing friction for users considering larger projects. Overall, the design should reflect a business that values craftsmanship, transparency, and long-term relationships with its customers.

Target Market(s)

Retail Flooring Customers who purchase Hardwood, Engineered, Laminate, Vinyl & Tile. Not carpet

Industry/Entity Type

Flooring Store

Number of Pages Required

3 page

Font styles to use
Sans Serif

Colors

Designer to choose colors to be used in the design.

Requirements
Must have
• We like these two designs (Home Pages) https://www.talvenfloors.com/ https://mirelopaving.ca/
Nice to have
• We need a home page and two interior pages. The website will have 20+ pages coded by our developer, but we will use one home page design and 2 alternating interior pages to fill the website.

```html
<!DOCTYPE html>
<html lang="en">
<head>
<meta charset="utf-8">
<title>Talven Flooring – Tulsa Flooring Store</title>
<link href="https://fonts.googleapis.com/css2?family=Montserrat:wght@400;500;600;700;800&display=swap" rel="stylesheet">
<style>
:root{
  --red:#d0111f;
  --red-dark:#b10d19;
  --ink:#1c1c1c;
  --text:#333333;
  --dark:#353535;
  --dark-2:#2b2b2b;
  --pink:#fde9ec;
  --panel:#f3f4f3;
  --white:#ffffff;
  --font:'Montserrat', Arial, sans-serif;
}
*{box-sizing:border-box;margin:0;padding:0}
html,body{width:1200px;height:3878px;overflow:hidden}
body{font-family:var(--font);color:var(--text);background:var(--white);position:relative}
.abs{position:absolute}
.btn{position:absolute;display:flex;align-items:center;justify-content:center;background:var(--red);color:var(--white);font-weight:800;font-size:14px;text-transform:uppercase;letter-spacing:.2px;clip-path:polygon(0 0,100% 0,calc(100% - 16px) 100%,0 100%);text-decoration:none}
.btn.dark{background:var(--dark-2)}
.heading{position:absolute;left:0;width:1200px;text-align:center;font-weight:800;text-transform:uppercase;font-size:28px;color:var(--ink);letter-spacing:.3px;line-height:36px}
.heading .rule{display:inline-block;width:56px;height:3px;background:var(--red);vertical-align:middle;margin:0 20px 6px}
.para{position:absolute;left:0;width:1200px;text-align:center;font-size:13.5px;line-height:24px}
.lead{position:absolute;left:0;width:1200px;text-align:center;font-size:17px;font-weight:700;color:var(--ink)}

/* header */
.topbar{left:437px;top:0;width:763px;height:39px;background:var(--dark-2);clip-path:polygon(22px 0,100% 0,100% 100%,0 100%);display:flex;align-items:center;color:var(--white);font-size:14px}
.topbar .item{display:flex;align-items:center;gap:8px;margin-left:52px}
.topbar .item:first-child{margin-left:55px}
.topbar .visit{position:absolute;right:0;top:0;height:39px;width:229px;background:var(--red);display:flex;align-items:center;justify-content:center;font-weight:800;font-size:14px;text-transform:uppercase;clip-path:polygon(14px 0,100% 0,100% 100%,0 100%)}
.brand{left:112px;top:16px;display:flex;align-items:center;gap:12px}
.brand .mark{width:30px;height:30px;background:var(--red)}
.brand .name{font-size:30px;font-weight:800;color:var(--ink);letter-spacing:-.3px}
.nav{left:425px;top:63px;display:flex;gap:26px;font-size:12px;text-transform:uppercase;color:#444}
.nav .active{color:var(--red);font-weight:600;border-bottom:2px solid var(--red);padding-bottom:3px}

/* hero */
.hero{left:0;top:100px;width:1200px;height:519px;overflow:hidden}
.hero .photo{position:absolute;inset:0;background:linear-gradient(100deg,#c9c5bd 0%,#e9e7e2 45%,#f3f2ee 65%,#b9b5ab 100%)}
.hero .shade{position:absolute;inset:0;background:linear-gradient(160deg,#4a4a4a 0%,#2f2f2f 60%,#3a3a3a 100%);clip-path:polygon(0 0,705px 0,600px 100%,0 100%)}
.hero h1{position:absolute;left:120px;top:68px;width:500px;color:var(--white);font-size:27px;line-height:36px;font-weight:800;text-transform:uppercase}
.hero p{position:absolute;left:120px;top:190px;width:500px;color:#eee;font-size:13px;line-height:25.6px}

/* products */
.card{position:absolute;top:864px;width:306px;height:235px}
.card .img{position:absolute;inset:0;border-radius:4px}
.card .tab{position:absolute;left:0;bottom:0;width:275px;height:58px;background:var(--white);clip-path:polygon(0 0,92% 0,100% 100%,0 100%);display:flex;align-items:flex-end;justify-content:center;padding:0 24px 0 0;text-align:center;font-size:17px;font-weight:500;color:var(--ink);line-height:26px}
.arrow{position:absolute;top:974px;width:46px;height:46px;border-radius:50%;display:flex;align-items:center;justify-content:center}

/* services */
.services{left:0;top:1336px;width:1200px;height:610px;background:linear-gradient(135deg,#3c3c3c 0%,#333 50%,#3d3d3d 100%)}
.svc{position:absolute;top:269px;width:283px;height:192px;border:1.5px solid #bbb;border-radius:6px;background:rgba(40,40,40,.55);text-align:center;color:var(--white)}
.svc .tick{position:absolute;left:102px;top:23px;width:79px;height:79px;border-radius:50%;background:var(--red);display:flex;align-items:center;justify-content:center}
.svc .label{position:absolute;left:10px;right:10px;top:116px;font-size:17px;font-weight:700;line-height:27px}

/* why */
.why{left:119px;top:2199px;width:959px;height:206px;background:var(--panel);border:1.5px solid #444;display:flex;padding:22px 0}
.why .col{flex:1;text-align:center;border-right:1px solid #bbb;padding-top:5px}
.why .col:last-child{border-right:none}
.why .col svg{display:block;margin:0 auto 16px}
.why .col span{display:block;font-size:17px;font-weight:500;color:var(--ink);line-height:26.5px;padding:0 12px}

/* showroom */
.show-frame{left:119px;top:2593px;width:432px;height:374px;background:var(--red);border-radius:6px}
.show-photo{left:136px;top:2610px;width:432px;height:375px;border-radius:6px;background:linear-gradient(135deg,#8a8f96 0%,#6f6d6a 40%,#9a948c 70%,#5f6368 100%)}
.show-title{left:619px;top:2633px;font-size:28px;font-weight:800;line-height:36px;text-transform:uppercase;color:var(--ink)}
.show-text{left:619px;top:2709px;width:445px;font-size:13.5px;line-height:24px}

/* serving */
.pink-band{left:0;top:3233px;width:1200px;height:645px;background:var(--pink)}
.map{left:670px;top:3060px;width:432px;height:375px;background:linear-gradient(135deg,#f2e6c9 0%,#e9ddbf 40%,#d8e2c8 70%,#efe3c6 100%)}
.serve{left:95px;top:3084px;width:760px;height:322px;background:var(--red);border-radius:6px;clip-path:polygon(0 0,643px 0,100% 100%,0 100%)}
.serve h2{position:absolute;left:30px;top:56px;color:var(--white);font-size:28px;line-height:36px;font-weight:800;text-transform:uppercase}
.serve p{position:absolute;left:30px;top:126px;width:600px;color:var(--white);font-size:13.5px;line-height:24px}

/* footer */
.foot-brand{left:136px;top:3513px;display:flex;align-items:center;gap:10px}
.foot-brand .mark{width:28px;height:28px;background:var(--red)}
.foot-brand .name{font-size:28px;font-weight:800;color:var(--ink)}
.foot-h{position:absolute;top:3493px;font-size:17px;font-weight:600;text-transform:uppercase;color:var(--ink);letter-spacing:.3px}
.foot-links{left:420px;top:3531px;list-style:none;font-size:14.5px;color:#444}
.foot-links li{height:32px;display:flex;align-items:center;gap:10px}
.contact-row{position:absolute;left:614px;display:flex;gap:14px;font-size:14.5px;line-height:24px;color:#444}
.contact-row .ic{width:30px;height:30px;border-radius:50%;background:var(--red);display:flex;align-items:center;justify-content:center;flex:none}
.news{left:844px;top:3540px;width:230px;font-size:11px;line-height:21px;color:#555}
.email{left:846px;top:3635px;width:227px;height:41px;background:var(--white);border:1px solid #ccc;border-radius:6px;display:flex;align-items:center;padding-left:14px;font-size:12px;color:#555}
.email .send{position:absolute;right:0;top:0;width:41px;height:39px;background:var(--red);border-radius:0 6px 6px 0;display:flex;align-items:center;justify-content:center}
.foot-line{left:117px;top:3809px;width:960px;height:1px;background:#555}
.copy{left:0;top:3838px;width:1200px;text-align:center;font-size:13px;color:#333}
</style>
</head>
<body>

<div class="abs brand"><span class="name">Talven Flooring</span><span class="mark"></span></div>
<div class="abs topbar">
  <div class="item">
    <svg width="20" height="20" viewBox="0 0 24 24" fill="none" stroke="#fff" stroke-width="1.8"><path d="M5 3h4l2 5-3 2a12 12 0 0 0 6 6l2-3 5 2v4a2 2 0 0 1-2 2A17 17 0 0 1 3 5a2 2 0 0 1 2-2z"/></svg>
    (918) 555-0142
  </div>
  <div class="item">
    <svg width="18" height="22" viewBox="0 0 24 28" fill="none" stroke="#fff" stroke-width="1.8"><path d="M12 26s9-9 9-15a9 9 0 0 0-18 0c0 6 9 15 9 15z"/><circle cx="12" cy="11" r="3"/></svg>
    2450 E Harlan St, Tulsa, OK 74137
  </div>
  <div class="visit">Visit the showroom</div>
</div>
<nav class="abs nav">
  <span class="active">Home</span><span>Products</span><span>Services</span><span>Reviews</span><span>Financing</span><span>Inspiration</span><span>About us</span><span>Contact</span>
</nav>

<section class="abs hero">
  <div class="photo" role="img" aria-label="Bright modern living room with light wood flooring and large windows"></div>
  <div class="shade"></div>
  <h1>Tulsa’s local flooring store for quality materials &amp; expert installation</h1>
  <p>Talven Flooring is a locally owned flooring store in Tulsa offering quality flooring products, professional installation, and hardwood floor refinishing—all from one trusted team. From our Tulsa showroom, we help homeowners and contractors choose flooring that fits theirspace, lifestyle, and budget, then install it with care and precision.<br>Whether you’re building, remodeling, or restoring existing floors, we provide straightforward guidance, skilled workmanship, and results that last.</p>
  <a class="btn" style="left:120px;top:397px;width:242px;height:39px">Explore our floorings</a>
</section>

<h2 class="heading" style="top:694px"><span class="rule"></span>Flooring products for every space<span class="rule"></span></h2>
<p class="para" style="top:748px">Our showroom features a carefully selected range of flooring options designed to perform well in Tulsa homes<br>and businesses. We carry flooring for both walls and floors, with styles ranging from classic to modern.</p>
<p class="lead" style="top:816px">Our flooring selection includes:</p>

<div class="arrow" style="left:55px;background:#fbd3d7">
  <svg width="26" height="26" viewBox="0 0 24 24" fill="none" stroke="#d0111f" stroke-width="2.6" stroke-linecap="round" stroke-linejoin="round"><path d="M20 12H5M11 5l-7 7 7 7"/></svg>
</div>
<div class="arrow" style="left:1103px;background:var(--red)">
  <svg width="26" height="26" viewBox="0 0 24 24" fill="none" stroke="#fff" stroke-width="2.6" stroke-linecap="round" stroke-linejoin="round"><path d="M4 12h15M13 5l7 7-7 7"/></svg>
</div>

<div class="card" style="left:120px">
  <div class="img" role="img" aria-label="Dining room with solid hardwood flooring" style="background:linear-gradient(135deg,#ece9e2,#c9b9a0 60%,#b89d7a)"></div>
  <div class="tab" style="height:62px;align-items:center;padding-top:6px">Solid hardwood<br>flooring</div>
</div>
<div class="card" style="left:447px">
  <div class="img" role="img" aria-label="Office with engineered hardwood flooring" style="background:linear-gradient(135deg,#eeeeec,#d6d3cc 55%,#c2ab84)"></div>
  <div class="tab" style="height:62px;align-items:center;padding-top:6px">Engineered hardwood<br>flooring</div>
</div>
<div class="card" style="left:772px">
  <div class="img" role="img" aria-label="Kitchen with laminate flooring" style="background:linear-gradient(135deg,#e4e4e2,#c7c6c2 55%,#a8a49d)"></div>
  <div class="tab" style="height:62px;align-items:center;padding-top:6px">Laminate flooring</div>
</div>

<a class="btn" style="left:185px;top:1141px;width:174px;height:41px">Explore more</a>
<a class="btn" style="left:513px;top:1141px;width:174px;height:41px">Explore more</a>
<a class="btn" style="left:838px;top:1141px;width:174px;height:41px">Explore more</a>

<p class="para" style="top:1226px">As a full-service flooring store, we make it easy to compare materials, finishes, and styles in<br>person before making a decision.</p>

<section class="abs services" role="img" aria-label="Dimmed kitchen interior background">
  <h2 class="heading" style="top:69px;color:#fff"><span class="rule"></span>Professional installation &amp;<span class="rule"></span><br>refinishing services</h2>
  <p class="para" style="top:159px;color:#eee">In addition to selling flooring, Talven Flooring provides expert installation and refinishing services.<br>Our experienced team handles projects of all sizes with attention to detail and clear communication from start to finish.</p>
  <p class="lead" style="top:222px;color:#fff">Our services include:</p>

  <div class="svc" style="left:139px">
    <div class="tick"><svg width="54" height="54" viewBox="0 0 24 24" fill="none" stroke="#fff" stroke-width="1.6" stroke-linecap="round" stroke-linejoin="round"><path d="M20 12a8 8 0 1 1-4-6.9"/><path d="M8 12l3 3 9-9"/></svg></div>
    <div class="label">Flooring installation for all<br>material types</div>
  </div>
  <div class="svc" style="left:458px">
    <div class="tick"><svg width="54" height="54" viewBox="0 0 24 24" fill="none" stroke="#fff" stroke-width="1.6" stroke-linecap="round" stroke-linejoin="round"><path d="M20 12a8 8 0 1 1-4-6.9"/><path d="M8 12l3 3 9-9"/></svg></div>
    <div class="label">Hardwood floor<br>refinishing</div>
  </div>
  <div class="svc" style="left:777px">
    <div class="tick"><svg width="54" height="54" viewBox="0 0 24 24" fill="none" stroke="#fff" stroke-width="1.6" stroke-linecap="round" stroke-linejoin="round"><path d="M20 12a8 8 0 1 1-4-6.9"/><path d="M8 12l3 3 9-9"/></svg></div>
    <div class="label">Water damage restoration<br>related to flooring</div>
  </div>

  <p class="para" style="top:491px;color:#eee">By working with one company for both materials and labor, you avoid delays,<br>miscommunication, and unnecessary complications.</p>
</section>

<h2 class="heading" style="top:2015px"><span class="rule"></span>More than a flooring store<span class="rule"></span></h2>
<p class="para" style="top:2072px">What sets Talven Flooring apart is experience and craftsmanship. We work closely with homeowners and<br>contractors to ensure every project is done correctly, from subfloor preparation to final trim details.</p>
<p class="lead" style="top:2139px">Customers choose us because we offer:</p>

<div class="abs why">
  <div class="col">
    <svg width="56" height="58" viewBox="0 0 56 58" fill="none" stroke="#222" stroke-width="2"><rect x="10" y="4" width="36" height="8"/><path d="M4 20h48v6H4z"/><rect x="8" y="26" width="40" height="28"/><rect x="14" y="32" width="14" height="14"/><rect x="32" y="32" width="10" height="22"/><path d="M4 54h48"/></svg>
    <span>A local Tulsa<br>showroom</span>
  </div>
  <div class="col">
    <svg width="58" height="58" viewBox="0 0 58 58" fill="none" stroke="#222" stroke-width="2"><circle cx="22" cy="34" r="11"/><circle cx="22" cy="34" r="4"/><path d="M22 19v4M22 45v4M7 34h4M33 34h4M11 23l3 3M30 42l3 3M11 45l3-3M30 26l3-3"/><path d="M38 22l14-14M48 6l6 6-4 2-4-4z"/></svg>
    <span>Skilled installers and<br>finishers</span>
  </div>
  <div class="col">
    <svg width="58" height="58" viewBox="0 0 58 58" fill="none" stroke="#222" stroke-width="2"><circle cx="29" cy="24" r="18"/><circle cx="29" cy="24" r="12"/><path d="M23 24l4 4 8-8"/><path d="M18 38l-6 16 8-3 4 6 5-13M40 38l6 16-8-3-4 6-5-13"/></svg>
    <span>Honest<br>recommendations, not<br>pressure</span>
  </div>
  <div class="col">
    <svg width="58" height="58" viewBox="0 0 58 58" fill="none" stroke="#222" stroke-width="2"><circle cx="32" cy="16" r="10"/><path d="M28 16l3 3 5-6"/><path d="M4 44l10-8h12l8 4h8l8-6 4 4-14 12H18l-6 4z"/></svg>
    <span>Quality products<br>selected for long-term<br>performance</span>
  </div>
</div>

<p class="para" style="top:2440px">Whether you’re visiting us as a flooring store or a tile store, our focus is on helping you<br>make informed decisions that add lasting value to your space.</p>
<a class="btn" style="left:455px;top:2510px;width:289px;height:41px">Schedule a consultation</a>

<div class="abs show-frame"></div>
<div class="abs show-photo" role="img" aria-label="Hand fanning through flooring material samples in the showroom"></div>
<h2 class="abs show-title">Visit our Tulsa <span style="display:inline-block;width:56px;height:3px;background:var(--red);vertical-align:middle;margin:0 0 6px 14px"></span><br>showroom</h2>
<p class="abs show-text">Choosing flooring online only goes so far. Seeing materials in person makes a real difference. We invite you to visit the Talven Flooring showroom in Tulsa, where you can explore hardwood, LVP, laminate, and tile options—including wall tile and floor tile—side by side.<br>Our team is happy to answer questions, explain differences between materials, and help you plan your next project.</p>
<a class="btn" style="left:619px;top:2905px;width:172px;height:39px">Contact us</a>

<div class="abs pink-band"></div>
<div class="abs map" role="img" aria-label="Road map of Tulsa and surrounding communities"></div>
<div class="abs serve">
  <h2>Serving Tulsa &amp;<br>surrounding areas <span style="display:inline-block;width:56px;height:3px;background:#fff;vertical-align:middle;margin:0 0 6px 14px"></span></h2>
  <p>Talven Flooring proudly serves Tulsa and nearby communities with reliable flooring products and professional service. Whether you’re updating a single room or planning a full renovation, we’re here to help from start to finish.</p>
  <a class="btn dark" style="left:30px;top:220px;width:172px;height:41px">Contact us</a>
</div>

<div class="abs foot-brand"><span class="name">Talven Flooring</span><span class="mark"></span></div>

<div class="foot-h" style="left:420px">Main links</div>
<ul class="abs foot-links">
  <li><svg width="12" height="12" viewBox="0 0 12 12"><path d="M1 6h9M6 2l4 4-4 4" fill="none" stroke="#333" stroke-width="1.6"/></svg>Home</li>
  <li><svg width="12" height="12" viewBox="0 0 12 12"><path d="M1 6h9M6 2l4 4-4 4" fill="none" stroke="#333" stroke-width="1.6"/></svg>Products</li>
  <li><svg width="12" height="12" viewBox="0 0 12 12"><path d="M1 6h9M6 2l4 4-4 4" fill="none" stroke="#333" stroke-width="1.6"/></svg>Services</li>
  <li><svg width="12" height="12" viewBox="0 0 12 12"><path d="M1 6h9M6 2l4 4-4 4" fill="none" stroke="#333" stroke-width="1.6"/></svg>Reviews</li>
  <li><svg width="12" height="12" viewBox="0 0 12 12"><path d="M1 6h9M6 2l4 4-4 4" fill="none" stroke="#333" stroke-width="1.6"/></svg>Financing</li>
  <li><svg width="12" height="12" viewBox="0 0 12 12"><path d="M1 6h9M6 2l4 4-4 4" fill="none" stroke="#333" stroke-width="1.6"/></svg>Inspiration</li>
  <li><svg width="12" height="12" viewBox="0 0 12 12"><path d="M1 6h9M6 2l4 4-4 4" fill="none" stroke="#333" stroke-width="1.6"/></svg>About us</li>
  <li><svg width="12" height="12" viewBox="0 0 12 12"><path d="M1 6h9M6 2l4 4-4 4" fill="none" stroke="#333" stroke-width="1.6"/></svg>ContactHome</li>
</ul>

<div class="foot-h" style="left:617px">Contact us</div>
<div class="contact-row" style="top:3538px">
  <span class="ic"><svg width="14" height="16" viewBox="0 0 24 28" fill="none" stroke="#fff" stroke-width="2.4"><path d="M12 26s9-9 9-15a9 9 0 0 0-18 0c0 6 9 15 9 15z"/><circle cx="12" cy="11" r="3"/></svg></span>
  <span>2450 E Harlan St,<br>Tulsa, OK 74137</span>
</div>
<div class="contact-row" style="top:3600px">
  <span class="ic"><svg width="14" height="14" viewBox="0 0 24 24" fill="#fff"><path d="M5 3h4l2 5-3 2a12 12 0 0 0 6 6l2-3 5 2v4a2 2 0 0 1-2 2A17 17 0 0 1 3 5a2 2 0 0 1 2-2z"/></svg></span>
  <span style="line-height:30px">(918) 555-0142</span>
</div>

<div class="foot-h" style="left:840px">Newsletter sign up</div>
<p class="abs news">To stay up to date on all things Talven flooring , drop your e-mail below if you would like to be sent any future promotions or deals</p>
<div class="abs email">Your Email Address
  <span class="send"><svg width="20" height="20" viewBox="0 0 24 24" fill="none" stroke="#fff" stroke-width="1.8" stroke-linejoin="round"><path d="M22 2L2 10l8 3 3 8z"/><path d="M22 2L10 13"/></svg></span>
</div>

<div class="abs foot-line"></div>
<p class="abs copy">© 2026 Talven Flooring | All Rights Reserved</p>

</body>
</html>
```